New business card design to go with our new logo

just want an eye-catching business card to go with our new logo. We are open to double sided or single sided. Just want it to have the following info on it. Whatever layout you think looks best.

First and Last Name
Title
Phone 801-555-7392
Address 214 W. Cedar Lane Pleasant Grove UT 84062
Email thecrew@marloweskennelandtreat.example

```html
<!DOCTYPE html>
<html lang="en">
<head>
<meta charset="utf-8">
<title>Marlowe's Kennel &amp; Treat — Business Card</title>
<link rel="stylesheet" href="https://fonts.googleapis.com/css2?family=Montserrat:wght@500;600;700&display=swap">
<style>
  :root {
    --sky: #25a6dc;
    --tangerine: #f4873c;
    --ink: #2b2b2b;
    --paper: #ffffff;
    --table: #d9d9d9;
  }
  * { box-sizing: border-box; margin: 0; padding: 0; }
  html, body { width: 1200px; height: 800px; overflow: hidden; }
  body {
    background: var(--table);
    font-family: "Montserrat", sans-serif;
    display: flex;
    flex-direction: column;
    align-items: center;
    justify-content: center;
    gap: 40px;
  }
  .card {
    width: 600px;
    height: 343px;
    position: relative;
    overflow: hidden;
    box-shadow: 0 6px 18px rgba(0,0,0,0.18);
  }

  /* Front */
  .card--front { background: var(--paper); }
  .brand-lockup {
    position: absolute;
    left: 40px;
    top: 0;
    width: 200px;
    height: 100%;
    display: flex;
    flex-direction: column;
    align-items: center;
    justify-content: center;
    gap: 14px;
  }
  .brand-mark {
    width: 56px; height: 56px;
    border-radius: 50%;
    border: 5px solid currentColor;
  }
  .brand-name {
    font-weight: 700;
    font-size: 30px;
    line-height: 1.05;
    text-align: center;
    letter-spacing: 0.5px;
  }
  .brand-name small { display: block; font-size: 15px; letter-spacing: 1.5px; margin-top: 4px; }
  .card--front .brand-lockup { color: var(--tangerine); }

  .divider {
    position: absolute;
    left: 262px;
    top: 78px;
    width: 2px;
    height: 160px;
    background: var(--tangerine);
  }
  .contact {
    position: absolute;
    left: 288px;
    top: 72px;
    color: var(--ink);
    font-weight: 500;
    font-size: 12.5px;
    line-height: 1.55;
  }
  .contact__name {
    color: var(--sky);
    font-weight: 700;
    font-size: 24px;
    letter-spacing: 0.5px;
    line-height: 1.1;
  }
  .contact__title {
    color: var(--tangerine);
    font-size: 13px;
    margin-bottom: 12px;
  }
  .contact__address { margin-bottom: 10px; }
  .contact__row { display: flex; align-items: center; gap: 8px; }
  .contact__row svg { width: 11px; height: 11px; flex: none; }

  .edge-band { position: absolute; bottom: 0; height: 9px; }
  .edge-band--sky { left: 0; width: 60%; background: var(--sky); clip-path: polygon(0 0, 100% 0, 98.5% 100%, 0 100%); }
  .edge-band--tangerine { right: 0; width: 41%; height: 6px; bottom: 9px; background: var(--tangerine); }

  /* Back */
  .card--back { background: var(--sky); }
  .card--back .brand-lockup {
    color: var(--paper);
    left: 0; width: 100%;
  }
  .card--back .brand-mark { width: 80px; height: 80px; border-width: 7px; }
  .card--back .brand-name { font-size: 46px; }
  .card--back .brand-name small { font-size: 20px; }
</style>
</head>
<body>
  <section class="card card--front" aria-label="Business card front">
    <div class="brand-lockup">
      <span class="brand-mark" aria-hidden="true"></span>
      <p class="brand-name">MARLOWE'S<small>KENNEL &amp; TREAT</small></p>
    </div>
    <span class="divider" aria-hidden="true"></span>
    <div class="contact">
      <h1 class="contact__name">DANIEL REYES</h1>
      <p class="contact__title">Director</p>
      <p class="contact__address">214 W. Cedar Lane<br>Pleasant Grove UT 84062</p>
      <p class="contact__row">
        <svg viewBox="0 0 12 12" aria-hidden="true"><path d="M2.5 1 L4.5 1 L5.2 3.6 L4 4.6 Q5 7 7.4 8 L8.4 6.8 L11 7.5 L11 9.5 Q10.5 11 9 11 Q1 10 1 3 Q1 1.5 2.5 1 Z" fill="#25a6dc"/></svg>
        801-555-7392
      </p>
      <p class="contact__row">
        <svg viewBox="0 0 12 12" aria-hidden="true"><rect x="0.8" y="2.5" width="10.4" height="7" rx="1" fill="none" stroke="#25a6dc" stroke-width="1.2"/><path d="M1 3 L6 6.8 L11 3" fill="none" stroke="#25a6dc" stroke-width="1.2"/></svg>
        thecrew@marloweskennelandtreat.example
      </p>
      <p class="contact__row">
        <svg viewBox="0 0 12 12" aria-hidden="true"><circle cx="6" cy="6" r="5" fill="none" stroke="#25a6dc" stroke-width="1.1"/><ellipse cx="6" cy="6" rx="2.2" ry="5" fill="none" stroke="#25a6dc" stroke-width="1"/><path d="M1 6 H11" stroke="#25a6dc" stroke-width="1"/></svg>
        www.marloweskennelandtreat.example
      </p>
    </div>
    <span class="edge-band edge-band--sky" aria-hidden="true"></span>
    <span class="edge-band edge-band--tangerine" aria-hidden="true"></span>
  </section>

  <section class="card card--back" aria-label="Business card back">
    <div class="brand-lockup">
      <span class="brand-mark" aria-hidden="true"></span>
      <p class="brand-name">MARLOWE'S<small>KENNEL &amp; TREAT</small></p>
    </div>
  </section>
</body>
</html>
```